Premium men's gut health supplement needs a bottle label designed

We’re velnora - a premium men’s wellness brand focused on gut health. Our first product is a high-quality daily supplement designed to support digestion, regularity, and internal cleanliness. Backed by science and tailored for modern lifestyles, velnora is crafted in the UK and proudly LGBT-owned. It aims to resolve intimacy problems that gay men may experience due to poor digestion but also does not exclude any other orientation - other men may use it simply to improve their digestion.

velnora is for health-conscious men who value science-backed supplements and want to feel confident from the inside out. Many of our early adopters will be gay and bisexual men who prioritise gut health as part of their self-care, sexual, and hygiene routine, though the product is equally effective and appealing to anyone seeking premium digestive support.

The product is premium the target customer is male, not specific to one location but primary markets will be US, UK and EU.

I’d like a supplement bottle designed for velnora, our premium men’s gut health brand. The focus should be clean, slightly clinical, and minimal - inspired by brands like Quelrin and Darvo. The key element is the wordmark (velnora) on the front, with no additional logo or icon. Lowercase text and a strong, contemporary font are preferred.

The bottle should be aesthetically pleasing so that people are proud to display it on their shelf, instead of hiding it in a cupboard (like Quelrin, darvo, Pia Venturek, Morvanel etc)

Avoid anything that shows the product as being for LGBT, e.g., no rainbows, men holding hands etc.

The design should be premium, minimalist and not be busy or overwhelming.

I have uploaded a file called "Bottle" to give an idea of the type of container, but please ignore the colours and change as you see fit. This is just for reference for the type of bottle we'll use - all colours are customisable.

I have also uploaded some images for "style" reference, e.g., darvo, quelrin, pia venturek, etc for inspiration.

```html
<!DOCTYPE html>
<html lang="en">
<head>
<meta charset="utf-8">
<title>velnora — Health Supplements Label</title>
<link rel="stylesheet" href="https://fonts.googleapis.com/css2?family=Jost:wght@300;400&display=swap">
<style>
  :root {
    --backdrop: #8a8a8a;
    --label-top: #2c2a2b;
    --label-bottom: #141213;
    --gold: #c9a25e;
    --gold-deep: #a8823f;
    --ink-light: #ecebea;
    --wave-tone: rgba(120, 118, 120, 0.22);
  }
  * { box-sizing: border-box; margin: 0; padding: 0; }
  html, body {
    width: 1200px;
    height: 829px;
    overflow: hidden;
    background: var(--backdrop);
  }
  .canvas {
    position: relative;
    width: 1200px;
    height: 829px;
  }
  .label {
    position: absolute;
    left: 284px;
    top: 34px;
    width: 632px;
    height: 760px;
    background: linear-gradient(175deg, var(--label-top) 0%, #222021 45%, var(--label-bottom) 100%);
    font-family: "Jost", sans-serif;
    overflow: hidden;
  }
  .wordmark {
    position: absolute;
    top: 104px;
    left: 0;
    width: 100%;
    text-align: center;
    font-weight: 300;
    font-size: 132px;
    line-height: 1;
    letter-spacing: -1px;
    color: var(--gold);
  }
  .rule {
    position: absolute;
    top: 289px;
    left: 76px;
    width: 480px;
    height: 2px;
    background: var(--gold);
  }
  .category {
    position: absolute;
    top: 306px;
    left: 0;
    width: 100%;
    text-align: center;
    font-weight: 400;
    font-size: 25px;
    letter-spacing: 3px;
    color: var(--ink-light);
  }
  .wave-field {
    position: absolute;
    left: 0;
    top: 460px;
    width: 632px;
    height: 270px;
    background: radial-gradient(ellipse 70% 45% at 35% 40%, var(--wave-tone), transparent 70%);
  }
  .details {
    position: absolute;
    top: 640px;
    left: 0;
    width: 100%;
    text-align: center;
    font-weight: 400;
    font-size: 24px;
    line-height: 34px;
    letter-spacing: 3px;
    color: var(--gold);
  }
  .base-band {
    position: absolute;
    left: 0;
    bottom: 10px;
    width: 100%;
    height: 8px;
    background: linear-gradient(90deg, var(--gold-deep), var(--gold), var(--gold-deep));
  }
</style>
</head>
<body>
  <main class="canvas">
    <section class="label">
      <h1 class="wordmark">velnora</h1>
      <div class="rule"></div>
      <p class="category">Health Supplements</p>
      <div class="wave-field" role="img" aria-label="Soft flowing line pattern in dark grey sweeping across the lower label"></div>
      <p class="details">For Man<br>30 Capsules</p>
      <div class="base-band"></div>
    </section>
  </main>
</body>
</html>
```